Gordon Pellbrook Consulting - Web Design Project

We need a web design for my new edgy consulting business specializing in innovation, technology and strategy.

It is our personal goal to turn each client into raving fans by helping them achieve their own business goals and aspirations through assisting them in raising their own innovation and marketing standards.

We provide our personalised and state-of-the-art services to our clients and boards who represent some of the world greatest innovative thinkers.
Updates

Here is some other information which may help shape your thinking.

I've had direct Involvement in the development of the following iPad, iPhone Applications and websites

FarbeyondOzlands.com (TerraLink platform) by Voyage Bureau
http://farbeyondozlands.example.au

Sail Verve by Bright Voyaging
https://apps.example-store.com/au/app/sail-verve/id100000001

uRedlandTR by Travel Territory Board
https://apps.example-store.com/au/app/uredlandtr/id100000002

Wexmoor Trips
http://www.wexmoortrips.example.au

Trek Mapper by Voyage Bureau
http://apps.example-store.com/au/app/trek-mapper/id100000003

Sunward by Sunward Travel Office
https://apps.example-store.com/au/app/sunward/id100000004

Upper Fernridge Valley Route by Visit Coastlands
https://apps.example-store.com/au/app/upper-fernridge-valley-route/id100000005

Wanderer Path by Travel Territory Board and Southern Plains Travel Council
https://apps.example-store.com/au/app/wanderers-path-grand-journey/id100000006

Gordon Pellbrook Consulting (GPC)
November 2012 – Present (8 months)Brisbane, Sydney, Canberra

Gordon’s consults to Small-to-Medium Enterprises (SME) and Government organisations on business strategy, technology strategy, risk mitigation, disruptive technology and innovation in the workplace.

Gordon’s consultancy mantra is that we cannot divorce economic life from cultural life particularly in an era when social capital may be as important as physical capital in business.

Reason: request from designers, I want to see their best efforts

Target Market(s)

35+

Industry/Entity Type

Business

Requirements
Must have
• Please use some of the personal image(s) contained in the zip files which can be downloaded from here

http://filedrop.example/k9Xq2Lm
http://filedrop.example/p4Rt7Vn
http://filedrop.example/z8Hw3Bc
Nice to have
• Black, Sleek design, maybe minimalist. Nice to have a Pixelle for the design. Nice to have it easily ported to Wordpress or be a modified Wordpress template. HTML 5, responsive design

```html
<!DOCTYPE html>
<html lang="en">
<head>
<meta charset="utf-8">
<title>Gordon Pellbrook Consulting</title>
<link href="https://fonts.googleapis.com/css2?family=PT+Sans:wght@400;700&display=swap" rel="stylesheet">
<style>
:root{
  --page:#141414;
  --panel:#2b2b2b;
  --panel-head:#353535;
  --green:#2fb34c;
  --text:#e6e6e6;
  --muted:#cfcfcf;
  --footer:#232323;
}
*{margin:0;padding:0;box-sizing:border-box}
html,body{width:990px;height:1200px;overflow:hidden;background:var(--page)}
body{font-family:"PT Sans",sans-serif;color:var(--text);position:relative}
.brand{position:absolute;left:117px;top:48px;display:flex;align-items:center;gap:10px}
.brand-mark{width:14px;height:14px;background:var(--green)}
.brand-name{font-size:22px;font-weight:400;color:var(--green);line-height:1}
.nav{position:absolute;left:107px;top:101px;width:776px;height:59px;background:linear-gradient(#3a3a3a,#2e2e2e);display:flex;align-items:center}
.nav a{color:#fff;text-decoration:none;font-size:13.5px;padding:0 13.3px;height:59px;line-height:59px}
.nav a.active{background:#262626;color:var(--green);padding:0 15px 0 25px}
.search{position:absolute;left:586px;top:21px;width:178px;height:22px;background:linear-gradient(#f3f3f3,#dcdcdc);border:1px solid #bbb;font-size:6px;color:#fff;padding:0 8px;line-height:20px}
.search svg{position:absolute;right:6px;top:5px}
.hero{position:absolute;left:107px;top:170px;width:776px;height:286px;background:linear-gradient(100deg,#8ba3bd 0%,#c9d3dc 40%,#e7ebee 60%,#b9c3cc 100%)}
.caption{position:absolute;left:107px;top:456px;width:776px;height:61px;background:var(--panel)}
.caption p{position:absolute;left:35px;top:22px;font-size:13px;color:#fff}
.dots{position:absolute;right:20px;top:24px;display:flex;gap:1px}
.dots span{width:12px;height:12px;border-radius:50%;border:1px solid #ddd;background:#555}
.dots span.on{background:#fff;box-shadow:inset 0 0 0 2px #555}
.card{position:absolute;top:544px;width:248px;height:137px;background:var(--panel)}
.card-head{margin-top:9px;height:43px;background:var(--panel-head);display:flex;align-items:center;padding-left:27px;gap:9px;color:var(--green);font-size:14px}
.card p{font-size:8.3px;line-height:16px;color:var(--muted);padding:15px 18px 0;text-align:justify}
.about-title{position:absolute;left:114px;top:705px;font-size:14px;font-weight:400;color:var(--green)}
.portrait{position:absolute;left:111px;top:733px;width:185px;height:239px;background:linear-gradient(#dfe3e6,#aeb8c2 60%,#8f9aa6)}
.about-text{position:absolute;left:305px;top:731px;width:314px;font-size:10.6px;line-height:16.5px;text-align:justify;color:var(--text)}
.jobs{position:absolute;left:635px;top:695px;width:248px;height:277px;background:var(--panel)}
.jobs h2{font-weight:400;font-size:14px;color:var(--green);padding:10px 16px}
.jobs ul{list-style:none;margin-top:7px}
.jobs li{font-size:10.5px;height:26.4px;padding-left:32px;position:relative;color:#f0f0f0}
.jobs li::before{content:"";position:absolute;left:15px;top:5px;width:5px;height:5px;background:var(--green)}
.partners{position:absolute;left:107px;top:1012px;width:776px;height:65px;background:linear-gradient(#d6d6d6,#c2c2c2);display:flex;align-items:center;justify-content:space-around;padding:0 28px;color:#3a3a3a;font-size:11px;font-weight:700}
.footer{position:absolute;left:0;top:1105px;width:990px;height:95px;background:var(--footer)}
.footer-nav{position:absolute;left:107px;top:23px;display:flex;gap:21px;font-size:10.8px}
.footer-nav a{color:#fff;text-decoration:none}
.copyright{position:absolute;left:110px;top:47px;font-size:10.8px;color:#fff}
.social{position:absolute;left:803px;top:37px;display:flex;gap:6px}
.social span{width:23px;height:23px;border-radius:50%;background:#fff}
</style>
</head>
<body>
<header class="brand">
  <span class="brand-mark"></span>
  <span class="brand-name">Gordon Pellbrook Consulting</span>
</header>

<nav class="nav">
  <a class="active" href="#">Home</a>
  <a href="#">About Us</a>
  <a href="#">Services</a>
  <a href="#">Clients</a>
  <a href="#">Candidates</a>
  <a href="#">Sitemap</a>
  <a href="#">Contact Us</a>
  <div class="search">Type search
    <svg width="11" height="11" viewBox="0 0 11 11"><circle cx="4.5" cy="4.5" r="3.3" fill="none" stroke="#999" stroke-width="1.3"/><line x1="7" y1="7" x2="10" y2="10" stroke="#999" stroke-width="1.5"/></svg>
  </div>
</nav>

<div class="hero" role="img" aria-label="Photo of a business team in discussion around a meeting table"></div>
<div class="caption">
  <p>"Neque porro quisquam est qui dolorem ipsum quia&nbsp; adipisci velit..."&nbsp; By&nbsp; Harold Brisk,CEO&nbsp; Novaline</p>
  <div class="dots"><span class="on"></span><span></span><span></span><span></span></div>
</div>

<section class="card" style="left:107px">
  <div class="card-head">
    <svg width="30" height="30" viewBox="0 0 30 30"><circle cx="13" cy="12" r="10" fill="#3a8fd6"/><rect x="5" y="20" width="22" height="6" rx="1" fill="#bbb"/></svg>
    Innovation
  </div>
  <p>Lorem Ipsum is simply dummy text of the rinting and typesetting industry. Lorem Ipsum has been the industry's standard dummy</p>
</section>
<section class="card" style="left:371px">
  <div class="card-head">
    <svg width="24" height="30" viewBox="0 0 24 30"><circle cx="12" cy="11" r="9" fill="#f5c91a"/><rect x="8" y="19" width="8" height="7" rx="1" fill="#999"/></svg>
    Technology
  </div>
  <p>Lorem Ipsum is simply dummy text of the rinting and typesetting industry. Lorem Ipsum has been the industry's standard dummy</p>
</section>
<section class="card" style="left:635px">
  <div class="card-head">
    <svg width="32" height="28" viewBox="0 0 32 28"><rect x="1" y="14" width="8" height="12" fill="#e8541e"/><rect x="11" y="8" width="8" height="18" fill="#f2a11b"/><rect x="21" y="2" width="8" height="24" fill="#3cb34a"/></svg>
    Startegy
  </div>
  <p>Lorem Ipsum is simply dummy text of the rinting and typesetting industry. Lorem Ipsum has been the industry's standard dummy</p>
</section>

<h2 class="about-title">About Me</h2>
<div class="portrait" role="img" aria-label="Portrait photo of the consultant in a grey suit"></div>
<p class="about-text">Lorem ipsum dolor sit amet, consectetur adipisicing elit, sed do eiusmod tempor incididunt ut labore et dolore magna aliqua. Ut enim ad minim veniam, quis nostrud exercitation ullamco laboris nisi ut aliquip ex ea commodo consequat. Duis aute irure dolor in reprehenderit in voluptate velit esse cillum dolore eu fugiat nulla pariatur. Excepteur sint occaecat cupidatat non proident, sunt in culpa qui officia deserunt mollit anim id est laborum.Lorem ipsum dolor sit amet, consectetur adipisicing elit, sed do eiusmod tempor incididunt ut labore et dolore magna aliqua.<br>Lorem ipsum dolor sit amet, consectetur adipisicing elit, sed do eiusmod tempor incididunt ut labore et dolore magna aliqua. Ut enim ad minim veniam, quis nostrud exercitation ullamco laboris nisi ut aliquip ex ea commodo consequat.Lorem ipsum dolor sit amet, consectetur adipisicing elit, sed do eiusmod tempor incididunt ut labore et dolore.</p>

<aside class="jobs">
  <h2>Job openings with us</h2>
  <ul>
    <li>Indian Kitchen Chef - Andaman</li>
    <li>Continental Chef - Chennai</li>
    <li>Sous Chef - Chennai</li>
    <li>German Translator</li>
    <li>Network Administrator</li>
    <li>Accounts Manager</li>
    <li>Chartered Accountant</li>
    <li>Chef - Pastries &amp; Confectioneries</li>
  </ul>
</aside>

<div class="partners">
  <span>Marwen</span><span>Velmora</span><span>Qasr</span><span>Brenna Bank</span><span>Qadira</span><span>Topnotch</span><span>Novaline</span><span>Larkin &amp; Co.</span><span>Dunmore Med</span>
</div>

<footer class="footer">
  <nav class="footer-nav">
    <a href="#">Home</a><a href="#">About Us</a><a href="#">Services</a><a href="#">Clients</a><a href="#">Candidates</a><a href="#">Sitemap</a><a href="#">Contact Us</a>
  </nav>
  <p class="copyright">©2013 Gordon Pellbrook Consulting | All Rights Reserved</p>
  <div class="social" aria-label="Social links"><span></span><span></span><span></span></div>
</footer>
</body>
</html>
```